Redesign of Medical App for Patients

• The Designer’s task is to provide a new fully-responsive design for our apps, and then code it using only basic html and CSS.
• Your design will be incorporated into our existing REACT native app.

Target Market(s)

Medical Patients

Industry/Entity Type

Medical

Coding

Coded - Design and coding required

Number of Pages Required

5+ page

Requirements
Must have
• Short list candidates will receive detailed briefing
Nice to have
• detailed briefing contains some of our ideas.

```html
<!DOCTYPE html>
<html lang="en">
<head>
<meta charset="utf-8">
<title>Patient App Redesign – Screen Flow</title>
<link rel="stylesheet" href="https://fonts.googleapis.com/css2?family=Inter:wght@400;500;600&display=swap">
<style>
:root{
  --bg:#dfecf6;
  --white:#ffffff;
  --brand:#1a8fc7;
  --brand-dark:#1581b6;
  --ink:#1d2329;
  --muted:#5d6670;
  --nav:#6d757d;
  --c-yellow:#fffbea;
  --c-mint:#eefbf5;
  --c-lav:#e8ebfa;
  --c-rose:#fdecef;
  --c-pink:#fcf0f9;
  --c-sky:#edf5fc;
  --c-green:#e9faef;
}
*{box-sizing:border-box;margin:0;padding:0}
html,body{width:1200px;height:650px;overflow:hidden}
body{background:var(--bg);font-family:"Inter",sans-serif;color:var(--ink);position:relative}
.label{position:absolute;top:42px;font-size:11px;color:var(--ink)}
.flow-arrow{position:absolute;top:305px;width:24px;height:18px}
.or{position:absolute;left:875px;top:307px;font-size:12px;font-weight:600}
.phone{position:absolute;top:65px;width:249px;height:540px;background:var(--white);border-radius:20px;overflow:hidden;box-shadow:0 14px 30px rgba(60,110,150,.14)}
.abs{position:absolute}

/* splash */
.splash-mark{left:88px;top:234px;width:72px;height:72px;border-radius:50%;background:var(--brand)}
.splash-name{left:0;width:249px;top:318px;text-align:center;font-size:13px;font-weight:600;color:var(--brand);letter-spacing:.04em}

/* home */
.hero-dot{left:40px;top:85px;width:54px;height:54px;border-radius:50%;background:var(--brand)}
.hero-photo{left:40px;top:76px;width:160px;height:140px}
.hero-ring{left:171px;top:214px;width:16px;height:16px;border-radius:50%;border:2px solid #7fb8d8}
.tagline{left:0;width:249px;top:269px;text-align:center;font-size:11px;font-weight:500;color:var(--brand)}
.home-title{left:0;width:249px;top:302px;text-align:center;font-size:14px;font-weight:500;line-height:16px}
.home-desc{left:0;width:249px;top:351px;text-align:center;font-size:9.5px;line-height:14px;color:var(--muted)}
.btn-start{left:30px;top:403px;width:190px;height:28px;border-radius:5px;background:var(--brand);color:var(--white);font-size:9.5px;font-weight:500;display:flex;align-items:center;justify-content:center;gap:8px}
.brand-row{left:0;width:249px;top:487px;display:flex;justify-content:center;align-items:center;gap:6px;font-size:10px;font-weight:500;color:var(--brand);letter-spacing:.02em}
.brand-row i{width:14px;height:14px;border-radius:50%;background:var(--brand)}
.meta{left:0;width:249px;top:510px;text-align:center;font-size:6.5px;line-height:10px;color:var(--muted)}

/* contents */
.status{left:12px;top:10px;font-size:9.5px;color:var(--white)}
.status-icons{right:14px;top:11px}
.menu-ico{left:7px;top:37px}
.gear-ico{right:8px;top:36px}
.head-v1{left:0;top:0;width:249px;height:155px;background:var(--brand)}
.title-v1{left:0;width:249px;top:65px;text-align:center;font-size:13px;font-weight:500;color:var(--white)}
.search{display:flex;align-items:center;justify-content:center;gap:6px;background:var(--white);font-size:8.5px;color:var(--ink)}
.search-v1{left:7px;top:92px;width:236px;height:26px;border-radius:2px}
.grid-card{width:115px;height:107px;border-radius:6px;padding:0 10px}
.card-ico{position:absolute;left:10px;top:40px;width:23px;height:23px;border-radius:50%}
.grid-card h3{position:absolute;left:10px;top:72px;font-size:11px;font-weight:500}
.grid-card p{position:absolute;left:10px;right:6px;top:86px;font-size:8px;line-height:10px;color:var(--muted)}

.head-v2{left:0;top:0;width:249px;height:152px;border-radius:0 0 16px 16px;background:linear-gradient(160deg,#6db9dc 0%,#2f9bcf 55%,#1a8ac2 100%)}
.title-v2{left:0;width:249px;top:65px;text-align:center;font-size:14px;font-weight:500;line-height:16px;color:var(--white)}
.search-v2{left:7px;top:116px;width:236px;height:27px;border-radius:14px}
.row-item{left:8px;width:235px;height:42px;border-radius:5px}
.row-item .card-ico{left:8px;top:10px}
.row-item h3{position:absolute;left:41px;top:7px;font-size:11.5px;font-weight:500}
.row-item p{position:absolute;left:41px;top:23px;font-size:8px;color:var(--muted);white-space:nowrap}

.bottom-nav{left:0;top:490px;width:249px;height:50px;background:var(--white);border-top:1px solid #eef1f4}
.nav-item{position:absolute;top:10px;width:46px;text-align:center;font-size:7.5px;color:var(--nav)}
.nav-item svg{display:block;margin:0 auto 3px}
.home-btn{position:absolute;left:110px;top:4px;width:30px;height:30px;border-radius:50%;background:var(--brand);display:flex;align-items:center;justify-content:center}
.home-bar{position:absolute;left:80px;top:43px;width:89px;height:3px;border-radius:2px;background:var(--ink)}

.ico-info{background:#f26b84}.ico-doc{background:#d466dc}.ico-proc{background:#4b82ef}
.ico-rec{background:#f5a524}.ico-home{background:#2fb98e}.ico-what{background:#ef7088}.ico-ok{background:#2bb57c}
.y{background:var(--c-yellow)}.m{background:var(--c-mint)}.l{background:var(--c-lav)}.r{background:var(--c-rose)}.p{background:var(--c-pink)}.s{background:var(--c-sky)}.g{background:var(--c-green)}
</style>
</head>
<body>

<div class="label" style="left:45px">Splash Screen</div>
<div class="label" style="left:330px">Home</div>
<div class="label" style="left:616px">Contents -&nbsp; Variation 1</div>
<div class="label" style="left:901px">Contents -&nbsp; Variation 2</div>

<svg class="flow-arrow" style="left:300px" viewBox="0 0 24 18"><path d="M1 9h21M14 2l8 7-8 7" fill="none" stroke="#1d2329" stroke-width="1.6"/></svg>
<svg class="flow-arrow" style="left:586px" viewBox="0 0 24 18"><path d="M1 9h21M14 2l8 7-8 7" fill="none" stroke="#1d2329" stroke-width="1.6"/></svg>
<div class="or">OR</div>

<!-- Splash -->
<section class="phone" style="left:45px">
  <div class="abs splash-mark"></div>
  <div class="abs splash-name">CARELOOP</div>
</section>

<!-- Home -->
<section class="phone" style="left:330px">
  <div class="abs hero-dot"></div>
  <svg class="abs hero-photo" viewBox="0 0 160 140" role="img" aria-label="Photo of a surgical team performing laparoscopic surgery with instruments on a tray">
    <defs><linearGradient id="op" x1="0" y1="0" x2="1" y2="1"><stop offset="0" stop-color="#c9dde6"/><stop offset=".5" stop-color="#8fb4c6"/><stop offset="1" stop-color="#3e6b82"/></linearGradient></defs>
    <path d="M112 8 Q100 -2 86 8 L8 100 Q-4 118 14 124 L140 138 Q160 140 158 120 L150 60 Q146 30 112 8Z" fill="url(#op)"/>
  </svg>
  <div class="abs hero-ring"></div>
  <div class="abs tagline">The Care Companion™</div>
  <h1 class="abs home-title">Laproscopic<br>Cholecystectomy</h1>
  <p class="abs home-desc">Everything you need to know before,<br>during, and after your surgery.</p>
  <div class="abs btn-start">Get Started <svg width="11" height="9" viewBox="0 0 11 9"><path d="M0 4.5h9.5M6 1l3.5 3.5L6 8" fill="none" stroke="#fff" stroke-width="1.3"/></svg></div>
  <div class="abs brand-row"><i></i>CARELOOP</div>
  <p class="abs meta">Version: 1.9.37-2022.04.06<br>Copyright 2022. CareLoop, Inc.</p>
</section>

<!-- Contents variation 1 -->
<section class="phone" style="left:616px">
  <div class="abs head-v1"></div>
  <svg class="abs" style="left:0;top:118px" width="249" height="45" viewBox="0 0 249 45"><path d="M0 30 Q40 5 95 22 T180 20 T249 12 V45 H0Z" fill="#fff"/><path d="M0 30 Q40 5 95 22 T180 20 T249 12" fill="none" stroke="#bfe0f0" stroke-width="4" opacity=".6"/></svg>
  <div class="abs status">16:20</div>
  <svg class="abs status-icons" width="28" height="8" viewBox="0 0 28 8"><rect x="0" y="1" width="6" height="6" fill="#cfe6f3"/><circle cx="13" cy="4" r="3.2" fill="#cfe6f3"/><path d="M19 1h8l-4 6z" fill="#cfe6f3"/></svg>
  <svg class="abs menu-ico" width="16" height="12" viewBox="0 0 16 12"><path d="M1 1h14M1 6h10M1 11h7" stroke="#fff" stroke-width="1.5" stroke-linecap="round"/></svg>
  <svg class="abs gear-ico" width="18" height="18" viewBox="0 0 18 18"><path d="M9 1.5l6.5 3.75v7.5L9 16.5 2.5 12.75v-7.5z" fill="none" stroke="#fff" stroke-width="1.4"/><circle cx="9" cy="9" r="2.4" fill="none" stroke="#fff" stroke-width="1.4"/></svg>
  <h2 class="abs title-v1">Laproscopic Cholecystectomy</h2>
  <div class="abs search search-v1"><svg width="11" height="11" viewBox="0 0 11 11"><circle cx="4.6" cy="4.6" r="3.6" fill="none" stroke="#1d2329" stroke-width="1.3"/><path d="M7.3 7.3L10 10" stroke="#1d2329" stroke-width="1.3"/></svg>Search for quick answers</div>

  <div class="abs grid-card y" style="left:7px;top:156px"><span class="card-ico ico-info"></span><h3>About Procedure</h3><p>Why and how is it done</p></div>
  <div class="abs grid-card m" style="left:128px;top:156px"><span class="card-ico ico-doc"></span><h3>Pre-Procedure</h3><p>How to get ready</p></div>
  <div class="abs grid-card l" style="left:7px;top:270px"><span class="card-ico ico-proc"></span><h3>Procedure</h3><p>The day of the procedure - in the operating room</p></div>
  <div class="abs grid-card r" style="left:128px;top:270px"><span class="card-ico ico-rec"></span><h3>Recovery</h3><p>Expectations immediately after surgery</p></div>
  <div class="abs grid-card p" style="left:7px;top:384px"><span class="card-ico ico-home"></span><h3>At Home</h3><p>How to care for yourself afterwards</p></div>
  <div class="abs grid-card s" style="left:128px;top:384px"><span class="card-ico ico-what"></span><h3>What to do if</h3><p>Responding to your issues</p></div>

  <nav class="abs bottom-nav">
    <div class="nav-item" style="left:2px"><svg width="16" height="11" viewBox="0 0 16 11"><circle cx="4" cy="3" r="2" fill="none" stroke="#555" stroke-width="1.2"/><circle cx="8" cy="3" r="2" fill="none" stroke="#555" stroke-width="1.2"/><circle cx="12" cy="3" r="2" fill="none" stroke="#555" stroke-width="1.2"/><path d="M1 10c0-3 14-3 14 0" fill="none" stroke="#555" stroke-width="1.2"/></svg>Your Team</div>
    <div class="nav-item" style="left:49px"><svg width="12" height="11" viewBox="0 0 12 11"><path d="M11 5.5H1.5M5 2L1.5 5.5 5 9" fill="none" stroke="#555" stroke-width="1.3"/></svg>Previous</div>
    <div class="home-btn"><svg width="13" height="13" viewBox="0 0 13 13"><path d="M1.5 6L6.5 1.5 11.5 6v5.5h-10z" fill="none" stroke="#fff" stroke-width="1.4"/></svg></div>
    <div class="nav-item" style="left:155px"><svg width="12" height="11" viewBox="0 0 12 11"><path d="M1 5.5h9.5M7 2l3.5 3.5L7 9" fill="none" stroke="#555" stroke-width="1.3"/></svg>Next</div>
    <div class="nav-item" style="left:201px"><svg width="12" height="12" viewBox="0 0 12 12"><path d="M10 6a4 4 0 1 1-3-3.9M7 1h3.5v3.5M10.5 1L6 5.5" fill="none" stroke="#555" stroke-width="1.2"/></svg>Share it</div>
    <div class="home-bar"></div>
  </nav>
</section>

<!-- Contents variation 2 -->
<section class="phone" style="left:901px">
  <div class="abs head-v2" role="img" aria-label="Tinted photo of surgeons in an operating room behind the header"></div>
  <div class="abs status">16:20</div>
  <svg class="abs status-icons" width="28" height="8" viewBox="0 0 28 8"><rect x="0" y="1" width="6" height="6" fill="#cfe6f3"/><circle cx="13" cy="4" r="3.2" fill="#cfe6f3"/><path d="M19 1h8l-4 6z" fill="#cfe6f3"/></svg>
  <svg class="abs menu-ico" width="16" height="12" viewBox="0 0 16 12"><path d="M1 1h14M1 6h10M1 11h7" stroke="#fff" stroke-width="1.5" stroke-linecap="round"/></svg>
  <svg class="abs gear-ico" width="18" height="18" viewBox="0 0 18 18"><path d="M9 1.5l6.5 3.75v7.5L9 16.5 2.5 12.75v-7.5z" fill="none" stroke="#fff" stroke-width="1.4"/><circle cx="9" cy="9" r="2.4" fill="none" stroke="#fff" stroke-width="1.4"/></svg>
  <h2 class="abs title-v2">Laproscopic<br>Cholecystectomy</h2>
  <div class="abs search search-v2"><svg width="11" height="11" viewBox="0 0 11 11"><circle cx="4.6" cy="4.6" r="3.6" fill="none" stroke="#1d2329" stroke-width="1.3"/><path d="M7.3 7.3L10 10" stroke="#1d2329" stroke-width="1.3"/></svg>Search for quick answers</div>

  <div class="abs row-item y" style="top:162px"><span class="card-ico ico-info"></span><h3>About Procedure</h3><p>Why and how is it done</p></div>
  <div class="abs row-item m" style="top:211px"><span class="card-ico ico-doc"></span><h3>Pre-Procedure</h3><p>How to get ready</p></div>
  <div class="abs row-item l" style="top:260px"><span class="card-ico ico-proc"></span><h3>Procedure</h3><p>The day of the procedure - in the operating room</p></div>
  <div class="abs row-item r" style="top:309px"><span class="card-ico ico-rec"></span><h3>Recovery</h3><p>Expectations immediately after surgery</p></div>
  <div class="abs row-item p" style="top:358px"><span class="card-ico ico-home"></span><h3>At Home</h3><p>How to care for yourself afterwards</p></div>
  <div class="abs row-item s" style="top:407px"><span class="card-ico ico-what"></span><h3>What to do if</h3><p>Responding to your issues</p></div>
  <div class="abs row-item g" style="top:456px"><span class="card-ico ico-ok"></span><h3>Success</h3><p>Feedback and who did this app</p></div>

  <nav class="abs bottom-nav">
    <div class="nav-item" style="left:2px"><svg width="16" height="11" viewBox="0 0 16 11"><circle cx="4" cy="3" r="2" fill="none" stroke="#555" stroke-width="1.2"/><circle cx="8" cy="3" r="2" fill="none" stroke="#555" stroke-width="1.2"/><circle cx="12" cy="3" r="2" fill="none" stroke="#555" stroke-width="1.2"/><path d="M1 10c0-3 14-3 14 0" fill="none" stroke="#555" stroke-width="1.2"/></svg>Your Team</div>
    <div class="nav-item" style="left:49px"><svg width="12" height="11" viewBox="0 0 12 11"><path d="M11 5.5H1.5M5 2L1.5 5.5 5 9" fill="none" stroke="#555" stroke-width="1.3"/></svg>Previous</div>
    <div class="home-btn"><svg width="13" height="13" viewBox="0 0 13 13"><path d="M1.5 6L6.5 1.5 11.5 6v5.5h-10z" fill="none" stroke="#fff" stroke-width="1.4"/></svg></div>
    <div class="nav-item" style="left:155px"><svg width="12" height="11" viewBox="0 0 12 11"><path d="M1 5.5h9.5M7 2l3.5 3.5L7 9" fill="none" stroke="#555" stroke-width="1.3"/></svg>Next</div>
    <div class="nav-item" style="left:201px"><svg width="12" height="12" viewBox="0 0 12 12"><path d="M10 6a4 4 0 1 1-3-3.9M7 1h3.5v3.5M10.5 1L6 5.5" fill="none" stroke="#555" stroke-width="1.2"/></svg>Share it</div>
    <div class="home-bar"></div>
  </nav>
</section>

</body>
</html>
```